Fornello Oak Hearth Kitchen (restaurant)

Restaurant with a cool vibe.
We need a refresh of existing site. Appealing to a hip crowd of 25 or older age bracket (mid price to high small town). Constant changes food and cocktail menu. A vibing atmosphere with jazz funk hip music.
Must be able to scale for any device… phone/mobile device super important.
Instagram: @Velmora.Brisket
Website: velmorabrisket.example

Target Market(s)

25-55 age group

Number of Pages Required

1 page

Font styles to use
Sans Serif

Requirements
Must have
• Simple to navigate. Simplicity is the key to all sophistication.

Links/Buttons
Menu
Gift Cards
Reservations
Take Out
Contact Us
Should not have
• Please, nothing generic looking… no cookie cutter look. Originality

```html
<!DOCTYPE html>
<html lang="en">
<head>
<meta charset="utf-8">
<title>Fornello Oak Hearth Kitchen</title>
<link href="https://fonts.googleapis.com/css2?family=Lato:wght@400;700&family=Rokkitt:wght@400;500&display=swap" rel="stylesheet">
<style>
:root{
  --bg:#212121;
  --panel:#2c2c2c;
  --panel-dark:#1b1b1b;
  --text:#ffffff;
  --muted:#d6d6d6;
  --line:#5a5a5a;
  --gold:#f2c200;
  --fire:#c9641c;
}
*{margin:0;padding:0;box-sizing:border-box}
html,body{width:1200px;height:5338px;overflow:hidden}
body{background:var(--bg);color:var(--text);font-family:"Lato",sans-serif;position:relative}
.abs{position:absolute}
.serif{font-family:"Rokkitt",serif;font-weight:400}
.copy{font-size:12px;line-height:26px;color:var(--muted)}

/* hero */
.hero{left:0;top:0;width:1200px;height:788px;
  background:radial-gradient(ellipse 380px 300px at 430px 230px,#e07a22 0%,#8a3a10 35%,rgba(40,18,8,0) 75%),
  radial-gradient(ellipse 500px 160px at 700px 560px,#6e3516 0%,rgba(30,20,14,0) 80%),
  linear-gradient(180deg,#1a1410 0%,#2a1c14 60%,#212121 100%)}
.brand{left:180px;top:28px;text-align:center}
.brand-name{font-family:"Rokkitt",serif;font-size:26px;font-weight:500;letter-spacing:2px;line-height:28px}
.brand-sub{font-size:8px;letter-spacing:.5px;color:var(--muted)}
.nav{top:48px;right:150px;display:flex;gap:28px;font-size:13px}
.nav a{color:var(--text);text-decoration:none}
.hero-title{left:149px;top:268px;font-size:60px;line-height:68px}
.hero-text{left:150px;top:408px;width:440px;font-size:12.5px;line-height:26px}
.btn{border:2px solid #fff;color:#fff;font-size:12px;letter-spacing:.5px;display:flex;align-items:center;justify-content:center;text-decoration:none}
.hero-btn{left:149px;top:491px;width:168px;height:46px}

/* story */
.story-media{left:149px;top:912px;width:450px;height:311px;
  background:radial-gradient(ellipse 200px 160px at 380px 90px,#f0a040,#a24a14 60%,#4a2210 100%)}
.play{left:210px;top:125px}
.h2{font-size:33px}
.story-title{left:659px;top:932px}
.story-text{left:661px;top:1008px;width:400px}

/* why */
.why-title{left:0;width:1200px;top:1368px;text-align:center}
.card{background:var(--panel);text-align:center;padding-top:42px}
.card h3{font-family:"Rokkitt",serif;font-weight:400;font-size:19px;margin:20px 0 10px}
.card p{font-size:12px;line-height:26px;color:var(--muted);padding:0 38px}
.card svg{display:block;margin:0 auto}

/* menu */
.menu-band{left:0;top:1952px;width:1200px;height:780px;
  background:radial-gradient(ellipse 300px 200px at 350px 350px,#4a4338,rgba(0,0,0,0) 80%),
  radial-gradient(ellipse 300px 220px at 880px 330px,#4e4436,rgba(0,0,0,0) 80%),
  linear-gradient(180deg,#242424,#302c27 50%,#262626)}
.menu-title{left:0;width:1200px;top:2022px;text-align:center}
.tabs{left:0;width:1200px;top:2082px;display:flex;justify-content:center;gap:28px;font-size:12px}
.tabs span{padding-bottom:6px}
.tabs .active{border-bottom:2px solid #fff}
.dish{width:410px}
.dish-head{display:flex;justify-content:space-between;font-family:"Rokkitt",serif;font-size:19px;margin-bottom:12px}
.dish p{font-size:12px;line-height:26px;color:var(--muted);width:290px}
.rule{height:1px;background:var(--line)}

/* team */
.team-title{left:147px;top:2862px}
.team-text{left:149px;top:2940px;width:400px}
.team-photo{left:603px;top:2827px;width:450px;height:311px;
  background:linear-gradient(135deg,#4a4a44,#7a6a5a 45%,#3a3a36)}

/* booking */
.book{left:68px;top:3270px;width:1074px;height:419px;background:var(--panel)}
.book-title{left:0;width:1074px;top:50px;text-align:center}
.book-text{left:0;width:1074px;top:118px;text-align:center;font-size:12px;line-height:27px;color:var(--muted)}
.field{top:210px;height:43px;border:1px solid #cfcfcf;display:flex;align-items:center;justify-content:space-between;padding:0 18px;font-size:12px;color:var(--muted)}
.book-btn{left:446px;top:307px;width:168px;height:46px;border-width:1px}

/* testimonials */
.test-title{left:0;width:1200px;top:3754px;text-align:center}
.quote{left:250px;top:3838px;width:700px;text-align:center;font-size:12px;line-height:26px;color:var(--muted)}
.qmark{font-family:"Rokkitt",serif;font-size:56px;color:#fff;line-height:40px}
.author{left:0;width:1200px;top:3960px;text-align:center;font-size:24px}
.stars{left:0;width:1200px;top:4010px;text-align:center;color:var(--gold);font-size:16px;letter-spacing:1px}

/* strip + map */
.strip{left:0;top:4104px;width:1200px;height:242px;display:flex}
.strip div{flex:1}
.map{left:0;top:4346px;width:1200px;height:466px;
  background:linear-gradient(160deg,#eef0ea,#e4e7e2 50%,#dfe6ea)}
.pin{left:590px;top:4552px}

/* footer */
.footer{left:0;top:4812px;width:1200px;height:526px;background:var(--panel-dark)}
.f-brand{left:0;width:1200px;top:4866px;text-align:center}
.f-head{font-family:"Rokkitt",serif;font-size:19px;top:4968px}
.f-col{top:5030px;font-size:12px;line-height:26px;color:var(--muted)}
.contact-row{display:flex;align-items:center;gap:14px}
.f-copy{left:151px;top:5297px;font-size:11.5px;color:var(--muted)}
.socials{left:924px;top:5290px;display:flex;gap:9px}
.socials span{width:25px;height:25px;border:1.5px solid #ddd;border-radius:50%}
</style>
</head>
<body>

<section class="abs hero" role="img" aria-label="Photo of a pizza baking beside flames in a wood-fired oven"></section>
<div class="abs brand"><div class="brand-name">FORNELLO</div><div class="brand-sub">Oak Hearth Kitchen</div></div>
<nav class="abs nav"><a href="#">Area for</a><a href="#">Gift Cards</a><a href="#">Menu</a><a href="#">Contact Us</a><a href="#">Reservations</a><a href="#">Take Out</a></nav>
<h1 class="abs serif hero-title">Good Foods<br>Great Vibes</h1>
<p class="abs hero-text">A neighborhood restaurant in the heart of Ashbury. Offering a unique menu of wood fired eats, craft beer, cocktails and wine.</p>
<a class="abs btn hero-btn" href="#">VIEW OUR MENU</a>

<div class="abs story-media" role="img" aria-label="Video still of pizzas in front of the oven fire">
  <svg class="abs play" width="50" height="60" viewBox="0 0 50 60"><polygon points="0,0 50,30 0,60" fill="#fff"/></svg>
</div>
<h2 class="abs serif h2 story-title">Our Story</h2>
<p class="abs copy story-text">Lorem Ipsum is simply dummy text of the printing and typesetting industry. Lorem Ipsum has been the industry's standard dummy text ever since the 1500s, when an unknown printer took a galley of type and scrambled it to make a type specimen book. It has survived not only five centuries, but also the leap into electronic typesetting, remaining essentially unchanged.</p>

<h2 class="abs serif h2 why-title">Why Choose us?</h2>
<div class="abs card" style="left:153px;top:1438px;width:291px;height:291px">
  <svg width="52" height="52" viewBox="0 0 52 52" fill="none" stroke="#fff" stroke-width="2"><rect x="10" y="6" width="32" height="40"/><line x1="17" y1="16" x2="35" y2="16"/><line x1="17" y1="24" x2="35" y2="24"/><line x1="17" y1="32" x2="29" y2="32"/></svg>
  <h3>Menu for every taste</h3>
  <p>Lorem Ipsum is simply dummy text of the printing and typesetting industry.</p>
</div>
<div class="abs card" style="left:458px;top:1492px;width:288px;height:292px">
  <svg width="64" height="52" viewBox="0 0 64 52" fill="none" stroke="#fff" stroke-width="2"><circle cx="20" cy="32" r="12"/><circle cx="40" cy="30" r="14"/><path d="M30 16 l6 -10 M40 16 l-2 -10"/></svg>
  <h3>Always fresh ingredients</h3>
  <p>Lorem Ipsum is simply dummy text of the printing and typesetting industry.</p>
</div>
<div class="abs card" style="left:761px;top:1438px;width:290px;height:291px">
  <svg width="52" height="52" viewBox="0 0 52 52" fill="none" stroke="#fff" stroke-width="2"><path d="M16 28 a10 10 0 1 1 6 -16 a10 10 0 0 1 16 4 a8 8 0 0 1 -2 12 z"/><rect x="18" y="28" width="16" height="8"/><line x1="26" y1="36" x2="26" y2="48"/></svg>
  <h3>Experienced chefs</h3>
  <p>Lorem Ipsum is simply dummy text of the printing and typesetting industry.</p>
</div>

<section class="abs menu-band" role="img" aria-label="Dimmed photo of plated dishes on a table"></section>
<h2 class="abs serif h2 menu-title">Our Menu</h2>
<div class="abs tabs"><span>Shareables</span><span>Wood Fired Pizza</span><span>Salads</span><span>Sandwiches</span><span>Burgers</span><span class="active">Mains &amp; Pasta</span></div>

<div class="abs dish" style="left:150px;top:2208px"><div class="dish-head"><span>Sonoma Valley Pasta</span><span>$25</span></div><p>Grilled sausage, baby spinach, green peas, cremini mushroom, white wine &amp; butter, fresh ricotta, orecchiette pasta</p></div>
<div class="abs dish" style="left:617px;top:2208px"><div class="dish-head"><span>Chicken Souvlaki</span><span>$25</span></div><p>Grilled lemon &amp; herbed chicken skewers, house-made tzatziki, Greek village salad, garlic parm fries</p></div>
<div class="abs rule" style="left:150px;top:2352px;width:410px"></div>
<div class="abs rule" style="left:617px;top:2352px;width:434px"></div>
<div class="abs dish" style="left:150px;top:2376px"><div class="dish-head"><span>Shrimp Linguine</span><span>$27</span></div><p>Wild Argentinian shrimp, bay scallops, fresh lemon, sun-dried tomato, parmesan, butter &amp; white wine sauce, linguini pasta</p></div>
<div class="abs dish" style="left:617px;top:2376px"><div class="dish-head"><span>Buttermilk Fried Tenders</span><span>$20</span></div><p>Buttermilk fried chicken tenders, homemade jalapeño ranch &amp; garlic aioli for dipping, garlic parm fries</p></div>
<div class="abs rule" style="left:150px;top:2520px;width:410px"></div>
<div class="abs rule" style="left:617px;top:2520px;width:434px"></div>
<div class="abs dish" style="left:150px;top:2548px"><div class="dish-head"><span>Monterey Chicken</span><span>$25</span></div><p>Grilled chicken breast, garlic &amp; cilantro ricotta, fresh spinach, cremini mushroom, chickpeas, sweet corn</p></div>

<h2 class="abs serif h2 team-title">Our Team</h2>
<p class="abs copy team-text">Lorem Ipsum is simply dummy text of the printing and typesetting industry. Lorem Ipsum has been the industry's standard dummy text ever since the 1500s, when an unknown printer took a galley of type and scrambled it to make a type specimen book. It has survived not only five centuries, but also the leap into electronic typesetting, remaining essentially unchanged.</p>
<div class="abs team-photo" role="img" aria-label="Group photo of the restaurant team"></div>

<section class="abs book">
  <h2 class="abs serif h2 book-title">Book a table</h2>
  <p class="abs book-text">Lorem ipsum is simply dummy text of the printing and typesetting industry. Lorem Ipsum has been the industry's<br>standard dummy text ever since the 1500s</p>
  <div class="abs field" style="left:79px;width:284px"><span>How many persons?</span><svg width="16" height="16" viewBox="0 0 16 16" fill="none" stroke="#ddd" stroke-width="1.3"><circle cx="8" cy="5" r="3.5"/><path d="M1.5 15 a6.5 6 0 0 1 13 0"/></svg></div>
  <div class="abs field" style="left:386px;width:288px"><span>In which date</span><svg width="16" height="16" viewBox="0 0 16 16" fill="none" stroke="#ddd" stroke-width="1.3"><rect x="1.5" y="3" width="13" height="11.5"/><line x1="1.5" y1="6.5" x2="14.5" y2="6.5"/><line x1="5" y1="1" x2="5" y2="4"/><line x1="11" y1="1" x2="11" y2="4"/></svg></div>
  <div class="abs field" style="left:695px;width:288px"><span>Which Time?</span><svg width="16" height="16" viewBox="0 0 16 16" fill="none" stroke="#ddd" stroke-width="1.3"><circle cx="8" cy="8" r="6.5"/><path d="M8 4 v4 l3 2"/></svg></div>
  <a class="abs btn book-btn" href="#">RESERVATION</a>
</section>

<h2 class="abs serif h2 test-title">Testimonials</h2>
<svg class="abs" style="left:68px;top:3860px" width="40" height="18" viewBox="0 0 40 18" fill="none" stroke="#777" stroke-width="2"><path d="M40 9 H2 M10 1 L2 9 L10 17"/></svg>
<svg class="abs" style="left:1084px;top:3860px" width="40" height="18" viewBox="0 0 40 18" fill="none" stroke="#fff" stroke-width="2"><path d="M0 9 H38 M30 1 L38 9 L30 17"/></svg>
<span class="abs qmark" style="left:220px;top:3826px">“</span>
<p class="abs quote">Lorem Ipsum is simply dummy text of the printing and typesetting industry. Lorem Ipsum has been the industry's standard dummy text ever since the 1500s, when an unknown printer took a galley of type and scrambled it to make a type specimen book. It has survived not only five centuries, but also the leap into electronic typesetting, remaining essentially unchanged.</p>
<span class="abs qmark" style="left:690px;top:3916px">”</span>
<p class="abs serif author">Marcus Hale</p>
<p class="abs stars">★★★★★</p>

<div class="abs strip">
  <div role="img" aria-label="Photo of tacos" style="background:linear-gradient(135deg,#6b4a2a,#b0703a,#4a5a2a)"></div>
  <div role="img" aria-label="Photo of a grilled sandwich" style="background:linear-gradient(135deg,#c8b89a,#e0c070,#8a7050)"></div>
  <div role="img" aria-label="Photo of a pizza" style="background:linear-gradient(135deg,#5a2a1a,#a8421e,#6a5a3a)"></div>
  <div role="img" aria-label="Photo of a pasta dish" style="background:linear-gradient(135deg,#8a8070,#d8b878,#6a5a48)"></div>
  <div role="img" aria-label="Photo of a burger" style="background:linear-gradient(135deg,#3a3a3a,#a0703a,#d8d0c0)"></div>
</div>

<div class="abs map" role="img" aria-label="Street map showing the restaurant location"></div>
<svg class="abs pin" width="26" height="34" viewBox="0 0 26 34"><path d="M13 0 a13 13 0 0 1 13 13 c0 9 -13 21 -13 21 s-13 -12 -13 -21 a13 13 0 0 1 13 -13z" fill="#e53935"/><circle cx="13" cy="13" r="5" fill="#a11"/></svg>

<footer class="abs footer"></footer>
<div class="abs f-brand"><div class="brand-name">FORNELLO</div><div class="brand-sub">Oak Hearth Kitchen</div></div>
<h3 class="abs f-head" style="left:151px">Reservations</h3>
<h3 class="abs f-head" style="left:406px">Contact info.</h3>
<h3 class="abs f-head" style="left:665px">Quick Links</h3>
<h3 class="abs f-head" style="left:841px">Dining Hours</h3>
<p class="abs f-col" style="left:153px;width:220px">Reservations will not be available for the courtyard Under phase 1 and 2 of reopening. Walk-ins only. We can't wait to see you!</p>
<div class="abs f-col" style="left:410px">
  <div class="contact-row"><svg width="16" height="16" viewBox="0 0 16 16"><path d="M3 1 l3 0 1 4 -2 1.5 a9 9 0 0 0 4.5 4.5 l1.5 -2 4 1 0 3 a2 2 0 0 1 -2 2 A13 13 0 0 1 1 3 a2 2 0 0 1 2 -2z" fill="#fff"/></svg>555-014-0765</div>
  <div class="contact-row"><svg width="16" height="12" viewBox="0 0 16 12" fill="none" stroke="#fff" stroke-width="1.4"><rect x="1" y="1" width="14" height="10"/><path d="M1 1 l7 6 7 -6"/></svg>hello@velmorabrisket.example</div>
</div>
<div class="abs f-col" style="left:666px">Area for<br>Gift Cards<br>Menu<br>Contact Us<br>Reservations<br>Take Out</div>
<div class="abs f-col" style="left:843px">Courtyard is open<br>Thursday to Sunday<br>12:00pm – 9:00pm</div>
<h3 class="abs f-head" style="left:841px;top:5122px">Pickup &amp; Kitchen Hours</h3>
<div class="abs f-col" style="left:843px;top:5164px">Thursday to Sunday<br>12:00pm – 8:00pm</div>
<p class="abs f-copy">Copyright © 2021 Fornello Oak Hearth Kitchen. All Rights Reserved</p>
<div class="abs socials"><span></span><span></span><span></span><span></span></div>

</body>
</html>
```